I need a business card designed using the logo provided either vertical or horizontal......Crestmoor Property Partners is an Australian based real estate company that caters for the upper end of the market so the design of the business card "must reflect" the companies image!!
Colour combinations are optional but "must be realistic" and must be able to be accurately useable CMYK colours.
Please consider that any colours used "must be able to be used" and be suitable in following designs for "pull out banner signs" and "real estate signs".
The colours and the font in the attached designs are for example and other combinations are encouraged.
Target Market(s)
The High End of the Australian real estate market
Industry/Entity Type
Business
Contact Information for Business Card
Logo - Business Name - Director + Licensed Real Estate Agent - Mobile Number (Cell Phone) - Business Number - Fax - Email Address - Web address
Requirements
Must have
- Designs and colours (CMYK) that can easily be interpreted by an Australian printer.
Nice to have
- Some alternative ideas on colour and font..........the ones provided are ok and have been provided as an example but I am looking for alternative ideas
Should not have
- Loud, overly bright colours. Designs that do not reflect the professional standards of the business.
- Designs that look good on a computer monitor but can not be re-created on a printing press.............this is most important when it comes to shading etc.

```html
<!DOCTYPE html>
<html lang="en">
<head>
<meta charset="utf-8">
<title>Crestmoor Property Partners – Business Card</title>
<link rel="stylesheet" href="https://fonts.googleapis.com/css2?family=Michroma&family=Roboto+Condensed:wght@400;700&display=swap">
<style>
  :root {
    --backdrop: #e9e6df;
    --gold: #b0852c;
    --gold-dark: #9a7023;
    --khaki: #cfc596;
    --paper: #ffffff;
    --paper-shade: #ececec;
    --ink: #2a2a2a;
  }
  html, body {
    margin: 0;
    width: 1200px;
    height: 892px;
    overflow: hidden;
    background: var(--backdrop);
  }
  .card {
    position: absolute;
    left: 100px;
    top: 160px;
    width: 1000px;
    height: 572px;
    box-shadow: 0 10px 30px rgba(0,0,0,0.18);
  }
  .card-art { position: absolute; inset: 0; }
  .brand {
    position: absolute;
    left: 210px;
    top: 118px;
    display: flex;
    align-items: center;
    gap: 14px;
    font-family: "Michroma", sans-serif;
    font-size: 24px;
    letter-spacing: 2px;
    color: var(--ink);
    text-transform: uppercase;
    line-height: 1.3;
  }
  .brand-mark {
    width: 18px;
    height: 18px;
    background: var(--gold);
    flex: none;
  }
  .person {
    position: absolute;
    left: 210px;
    top: 215px;
    font-family: "Roboto Condensed", sans-serif;
  }
  .person-name {
    margin: 0;
    font-size: 60px;
    font-weight: 700;
    color: var(--gold);
    line-height: 1;
  }
  .person-title {
    margin: 6px 0 0 4px;
    font-size: 22px;
    font-weight: 400;
    color: var(--ink);
  }
  .contacts {
    position: absolute;
    left: 210px;
    top: 345px;
    margin: 0;
    padding: 0;
    list-style: none;
    font-family: "Roboto Condensed", sans-serif;
    font-size: 30px;
    color: var(--ink);
    line-height: 40px;
  }
  .contacts li { display: flex; align-items: center; gap: 16px; }
  .contact-icon { width: 20px; height: 20px; flex: none; }
</style>
</head>
<body>
  <div class="card">
    <svg class="card-art" viewBox="0 0 1000 572" width="1000" height="572" aria-hidden="true">
      <defs>
        <linearGradient id="paperFill" x1="0" y1="0" x2="0.4" y2="1">
          <stop offset="0" stop-color="var(--paper)"/>
          <stop offset="1" stop-color="var(--paper-shade)"/>
        </linearGradient>
      </defs>
      <rect class="frame-gold" width="1000" height="572" fill="var(--gold)"/>
      <polygon class="frame-khaki-left" points="0,0 330,0 300,40 70,40 70,250 40,290 0,290" fill="var(--khaki)"/>
      <polygon class="panel-white" points="70,40 300,40 330,0 330,40 960,40 960,532 70,532 70,260 40,290 70,250" fill="url(#paperFill)"/>
      <polygon class="panel-white-body" points="330,40 960,40 960,532 40,532 40,290 70,250 70,40" fill="url(#paperFill)"/>
      <polygon class="accent-khaki-right" points="790,40 960,40 960,300 900,300" fill="var(--khaki)"/>
      <polygon class="accent-gold-right" points="900,300 960,300 960,330" fill="var(--gold-dark)"/>
    </svg>

    <div class="brand">
      <span class="brand-mark"></span>
      <span class="brand-name">Crestmoor Property Partners</span>
    </div>

    <div class="person">
      <h1 class="person-name">Employee name</h1>
      <p class="person-title">Managing Director</p>
    </div>

    <ul class="contacts">
      <li>
        <svg class="contact-icon" viewBox="0 0 20 20"><path d="M5 2 L8 6 L6 8 C7 11 9 13 12 14 L14 12 L18 15 L16 18 C9 18 2 11 2 4 Z" fill="var(--gold)"/></svg>
        02 9481 3370
      </li>
      <li>
        <svg class="contact-icon" viewBox="0 0 20 20"><rect x="2" y="4" width="16" height="12" fill="var(--gold)"/><path d="M2 4 L10 11 L18 4" fill="none" stroke="#fff" stroke-width="1.5"/></svg>
        info@crestmoorpp.com.au
      </li>
      <li>
        <svg class="contact-icon" viewBox="0 0 20 20"><circle cx="10" cy="10" r="8" fill="var(--gold)"/><path d="M2 10 H18 M10 2 C6 6 6 14 10 18 M10 2 C14 6 14 14 10 18" fill="none" stroke="#fff" stroke-width="1.2"/></svg>
        www.crestmoorpp.com.au
      </li>
      <li>
        <svg class="contact-icon" viewBox="0 0 20 20"><path d="M10 1 C6 1 3.5 4 3.5 7.5 C3.5 12 10 19 10 19 C10 19 16.5 12 16.5 7.5 C16.5 4 14 1 10 1 Z" fill="var(--gold)"/><circle cx="10" cy="7.5" r="2.5" fill="#fff"/></svg>
        14 Harbour View Rd, Mosman NSW 2088
      </li>
    </ul>
  </div>
</body>
</html>
```